Deactivated Coal-Fired Power Plant to be redeveloped into a Green Energy Campus.

Want a striking business card statement that introduces our concept project to provide economic and community recovery to a former rural coal community in western PA.
Essentially 12 project representatives that will lead both the demolition of an existing power plant and the redevelopment to a new Green energy site.
Business Card should reflect our effort.
We are open to ideas.

Target Market(s)

Energy and Power Generation industries

Industry/Entity Type

Power Generation and Data Centers

Contact Information for Business Card

Included in uploaded materials

Font styles to use
Sans Serif
Other font styles liked:
• Arial, Calibri

Requirements
Must have
• Multiple colors

```html
<!DOCTYPE html>
<html lang="en">
<head>
<meta charset="utf-8">
<title>Ridgeline Renewal – Business Card</title>
<link rel="stylesheet" href="https://fonts.googleapis.com/css2?family=Montserrat:wght@400;500;600;700&display=swap">
<style>
  :root {
    --green: #129447;
    --black: #0a0a0c;
    --white: #ffffff;
    --ink: #1a1a1a;
    --backdrop: #2b2b2d;
  }
  * { margin: 0; padding: 0; box-sizing: border-box; }
  html, body {
    width: 1200px; height: 801px; overflow: hidden;
    background: var(--backdrop);
    font-family: "Montserrat", sans-serif;
  }
  .sheet {
    width: 1200px; height: 801px;
    display: flex; align-items: center; justify-content: center; gap: 40px;
  }
  .card {
    width: 540px; height: 309px;
    border-radius: 16px;
    border: 3px solid var(--green);
    position: relative;
    overflow: hidden;
  }
  .card--front { background: var(--black); display: flex; align-items: center; justify-content: center; }
  .card--back { background: var(--white); }

  .brand { display: flex; align-items: center; gap: 14px; font-weight: 700; letter-spacing: 0.02em; }
  .brand__dot { border-radius: 50%; background: var(--green); flex: none; }
  .card--front .brand { color: var(--white); font-size: 34px; }
  .card--front .brand__dot { width: 56px; height: 56px; }
  .card--back .brand { position: absolute; top: 40px; right: 34px; color: var(--ink); font-size: 20px; gap: 10px; }
  .card--back .brand__dot { width: 34px; height: 34px; }

  .contact { position: absolute; left: 38px; bottom: 30px; color: var(--ink); }
  .contact__name { color: var(--green); font-weight: 700; font-size: 24px; line-height: 1.1; }
  .contact__title { font-size: 13px; font-weight: 500; margin-top: 3px; }
  .contact__company { color: var(--green); font-size: 13px; font-weight: 600; margin-top: 14px; }
  .contact__city { font-size: 13px; font-weight: 500; margin-top: 2px; }
  .contact__lines { list-style: none; margin-top: 12px; }
  .contact__lines li { display: flex; align-items: center; gap: 10px; font-size: 13px; font-weight: 500; line-height: 21px; letter-spacing: 0.02em; }
  .icon { width: 14px; height: 14px; flex: none; fill: var(--green); }
</style>
</head>
<body>
<main class="sheet">
  <section class="card card--front" aria-label="Card front">
    <div class="brand"><span class="brand__dot"></span>RIDGELINE RENEWAL</div>
  </section>

  <section class="card card--back" aria-label="Card back">
    <div class="brand"><span class="brand__dot"></span>RIDGELINE RENEWAL</div>
    <div class="contact">
      <p class="contact__name">Daniel Marsh</p>
      <p class="contact__title">Chief Operation Officer</p>
      <p class="contact__company">Ridgeline Renewal LLC</p>
      <p class="contact__city">Alder Falls, Pennsylvania</p>
      <ul class="contact__lines">
        <li><svg class="icon" viewBox="0 0 16 16"><path d="M3.5 1 6 3.8 4.6 5.6c.9 2 2.6 3.8 4.8 4.8L11.2 9 14 11.5 12.4 14C6.5 13.6 2.4 9.5 2 3.6Z"/></svg>555.201.4400</li>
        <li><svg class="icon" viewBox="0 0 16 16"><path d="M4.5 1h7a1 1 0 0 1 1 1v12a1 1 0 0 1-1 1h-7a1 1 0 0 1-1-1V2a1 1 0 0 1 1-1Zm.5 2v9h6V3Zm3 10a.8.8 0 1 0 0 .01Z"/></svg>555.318.7200</li>
        <li><svg class="icon" viewBox="0 0 16 16"><path d="M1 3h14v10H1Zm1.5 1.2V12h11V4.2L8 8.6Z"/></svg>dmarsh@ridgelinerenewal.com</li>
        <li><svg class="icon" viewBox="0 0 16 16"><path d="M8 1a7 7 0 1 0 0 14A7 7 0 0 0 8 1Zm0 1.3c.8 0 1.7 1.5 2 3.7H6c.3-2.2 1.2-3.7 2-3.7ZM2.4 7h2.5a11 11 0 0 0 0 2H2.4a5.6 5.6 0 0 1 0-2Zm3.5 0h4.2a11 11 0 0 1 0 2H5.9a11 11 0 0 1 0-2Zm5.2 0h2.5a5.6 5.6 0 0 1 0 2h-2.5a11 11 0 0 0 0-2ZM6 10h4c-.3 2.2-1.2 3.7-2 3.7S6.3 12.2 6 10Z"/></svg>ridgelinerenewal.com</li>
      </ul>
    </div>
  </section>
</main>
</body>
</html>
```